FACEBOOK PAGE FOR BREVLO PLUMBING GROUP

We need a facebook banner for our new plumbing business.

Needs to be catchy and inline with our logo.

Phone: 0472 836 291
Email: hello@brevlo.com.au
website: www.brevlo.com.au
Servicing: Perth Metro Areas and surrounding suburbs
Services:
*We offer a wide range of services, including:
Plumbing – General maintenance, blocked drains, toilet repairs, burst pipes, reticulation, renovations & emergencies.

*Hot Water – Installation, servicing & repairs for all systems.

*Cooling & Heating – Air conditioning, evaporative cooling & heater servicing.

*Filtration – Filtered taps, under-sink systems & whole-house filtration setups.

Our Mission

Brevlo Group believes plumbing shouldn't break the bank - or your trust. Our mission is to provide honest, affordable, and no-nonsense plumbing services that get the job done right the first time. No runaround - just reliable work, and the respect every customer deserves.

What Makes Us Different???

Upfront Fixed Pricing
No surprises, no hidden fees. You get clear, honest quotes before any work begins.

Respectful, Customer-First Service
We show up on time, communicate clearly, and treat your property like it’s our own.

Locals Serving Locals
We’re proud to support the Perth community with reliable, high-quality plumbing backed by real local care.

FOR THE DESIGNER A little background on us as a new biz for your reference:
By Locals, For Locals
After 13 years in the plumbing industry, seasoned local plumber Wade founded his company to address the widespread issue of homeowners and businesses being overcharged or receiving inferior work. He knew there had to be a better way—and that’s when Brevlo was created.
Today, Brevlo Group is a trusted plumbing company based in Osborne Park, proudly serving residential, commercial, and industrial clients across the Perth metro area. With over a decade of experience, we deliver expert workmanship, fair pricing, and treat every job—big or small—with the same care and professionalism.
Need it done right—and affordably? Get it sorted with BREVLO now!

```html
<!DOCTYPE html>
<html lang="en">
<head>
<meta charset="utf-8">
<title>Brevlo Plumbing Group – Facebook Cover</title>
<link rel="stylesheet" href="https://fonts.googleapis.com/css2?family=Roboto+Condensed:wght@400;500;700;800&family=Poppins:wght@500;600;700&display=swap">
<style>
  :root {
    --navy: #1b2a8c;
    --royal: #2a4fc4;
    --royal-light: #3566d6;
    --sky: #3d92e0;
    --sky-light: #63b5f2;
    --white: #ffffff;
    --logo-navy: #2a2f7a;
    --photo-light: #e9eef3;
    --photo-blue: #2a46b8;
  }
  * { margin: 0; padding: 0; box-sizing: border-box; }
  html, body { width: 1200px; height: 1200px; overflow: hidden; background: #ffffff; }
  .cover {
    position: absolute; left: 60px; top: 364px;
    width: 1080px; height: 472px; overflow: hidden;
    background: radial-gradient(ellipse at 32% 45%, var(--royal-light) 0%, var(--royal) 45%, var(--navy) 100%);
    font-family: "Roboto Condensed", Arial, sans-serif;
    color: var(--white);
  }
  .cover__shapes { position: absolute; inset: 0; }
  .brand-tab {
    position: absolute; left: 176px; top: 0; width: 206px; height: 77px;
    background: var(--white); border-radius: 0 0 10px 10px;
    display: flex; align-items: center; justify-content: center; gap: 10px;
  }
  .brand-tab__name {
    font-family: "Poppins", Arial, sans-serif; font-weight: 600;
    font-size: 30px; letter-spacing: 4px; color: var(--logo-navy);
  }
  .brand-tab__dot { width: 14px; height: 14px; border-radius: 50%; background: var(--sky); }
  .headline {
    position: absolute; left: 40px; width: 470px; top: 96px; text-align: center;
  }
  .headline__title { font-weight: 800; font-size: 58px; line-height: 60px; letter-spacing: 1px; }
  .headline__area { font-weight: 500; font-size: 21px; line-height: 25px; letter-spacing: .5px; margin-top: 4px; }
  .intro-pill {
    position: absolute; left: 68px; top: 222px; width: 412px; height: 38px;
    border-radius: 19px; background: linear-gradient(180deg, var(--sky-light), #2f7fd6);
    box-shadow: 0 3px 8px rgba(10, 20, 80, .35);
    font-size: 20px; line-height: 38px; text-align: center; font-weight: 500;
  }
  .service { position: absolute; width: 230px; font-size: 13.5px; line-height: 14.5px; }
  .service__name { font-weight: 700; font-size: 17px; line-height: 18px; margin-bottom: 2px; }
  .service--left { text-align: right; right: 820px; }
  .service--right { text-align: left; left: 294px; }
  .service--plumbing { top: 280px; }
  .service--filtration { top: 284px; }
  .service--hotwater { top: 360px; }
  .service--cooling { top: 360px; }
  .divider-v { position: absolute; left: 276px; top: 285px; width: 1px; height: 136px; background: rgba(255,255,255,.75); }
  .divider-h { position: absolute; left: 187px; top: 351px; width: 180px; border-top: 1px dotted rgba(255,255,255,.7); }
  .contact-bar {
    position: absolute; left: 0; bottom: 0; width: 100%; height: 45px;
    background: var(--navy);
    font-family: "Poppins", Arial, sans-serif; font-weight: 500; font-size: 17px;
  }
  .contact { position: absolute; top: 0; height: 45px; display: flex; align-items: center; gap: 10px; }
  .contact--phone { left: 127px; }
  .contact--email { left: 435px; }
  .contact--web { left: 757px; }
  .contact__icon { width: 24px; height: 24px; border-radius: 6px; background: var(--sky); display: flex; align-items: center; justify-content: center; }
</style>
</head>
<body>
<div class="cover">
  <svg class="cover__shapes" width="1080" height="472" viewBox="0 0 1080 472">
    <path d="M480 0 C470 50 470 110 520 160 C570 215 540 270 508 330 C490 370 498 410 505 430 L1080 430 L1080 0 Z" fill="var(--sky)"/>
    <path role="img" aria-label="Photo: plumber in blue overalls and cap fixing a pipe under a white bathroom sink against a tiled wall"
      d="M518 0 C512 40 512 90 560 150 C605 205 585 250 562 300 C548 340 545 390 545 430 L1080 430 L1080 0 Z"
      fill="url(#photoTone)"/>
    <path d="M830 430 C850 385 930 370 990 395 C1015 405 1030 418 1040 430 Z" fill="rgba(255,255,255,.55)"/>
    <defs>
      <linearGradient id="photoTone" x1="0" y1="0" x2="1" y2="0.4">
        <stop offset="0" stop-color="var(--photo-light)"/>
        <stop offset="0.45" stop-color="#d6dfe8"/>
        <stop offset="0.75" stop-color="#5a78cc"/>
        <stop offset="1" stop-color="var(--photo-blue)"/>
      </linearGradient>
    </defs>
  </svg>

  <div class="brand-tab">
    <span class="brand-tab__name">BREVLO</span>
    <span class="brand-tab__dot"></span>
  </div>

  <div class="headline">
    <h1 class="headline__title">SERVICING</h1>
    <p class="headline__area">PERTH METRO AREAS AND<br>SURROUNDING SUBURBS</p>
  </div>

  <p class="intro-pill">We offer a wide range of services, including:</p>

  <div class="service service--left service--plumbing">
    <h2 class="service__name">PLUMBING</h2>
    <p>General maintenance, blocked drains,<br>toilet repairs, burst pipes, reticulation<br>renovations &amp; emergencies.</p>
  </div>
  <div class="service service--right service--filtration">
    <h2 class="service__name">FILTRATION</h2>
    <p>Filtered taps, under-sink systems &amp;<br>whole-house filtration setups.</p>
  </div>
  <div class="service service--left service--hotwater">
    <h2 class="service__name">HOT WATER</h2>
    <p>Installation, servicing &amp; repairs<br>for all systems.</p>
  </div>
  <div class="service service--right service--cooling">
    <h2 class="service__name">COOLING &amp; HEATING</h2>
    <p>Air conditioning, evaporative cooling<br>&amp; heater servicing.</p>
  </div>
  <span class="divider-v"></span>
  <span class="divider-h"></span>

  <div class="contact-bar">
    <div class="contact contact--phone">
      <span class="contact__icon"><svg width="14" height="14" viewBox="0 0 24 24"><path fill="#fff" d="M6.6 10.8a15.1 15.1 0 0 0 6.6 6.6l2.2-2.2a1 1 0 0 1 1-.25 11.4 11.4 0 0 0 3.6.57 1 1 0 0 1 1 1V20a1 1 0 0 1-1 1A17 17 0 0 1 3 4a1 1 0 0 1 1-1h3.5a1 1 0 0 1 1 1c0 1.25.2 2.45.57 3.57a1 1 0 0 1-.25 1z"/></svg></span>
      <span>0472 836 291</span>
    </div>
    <div class="contact contact--email">
      <span class="contact__icon"><svg width="15" height="12" viewBox="0 0 24 18"><rect x="1" y="1" width="22" height="16" rx="2" fill="none" stroke="#fff" stroke-width="2"/><path d="M2 2l10 8 10-8" fill="none" stroke="#fff" stroke-width="2"/></svg></span>
      <span>hello@brevlo.com.au</span>
    </div>
    <div class="contact contact--web">
      <span class="contact__icon"><svg width="15" height="15" viewBox="0 0 24 24" fill="none" stroke="#fff" stroke-width="2"><circle cx="12" cy="12" r="10"/><path d="M2 12h20M12 2c3 3 3 17 0 20M12 2c-3 3-3 17 0 20"/></svg></span>
      <span>www.brevlo.com.au</span>
    </div>
  </div>
</div>
</body>
</html>
```